Professional digital stationary

We need a digital stationary for our brand, we already have a logo and based on that we need a design for Word, Powerpoint, mailings and Linkedin. We need to be able to re use the stationary for other things like other social media. So basically what we ask is a template for Powerpoint and Word, some e-mail headers and a nice and professional Linkedin Header.

Target Market(s)

recruitment

Font styles to use
Sans Serif

```html
<!DOCTYPE html>
<html lang="en">
<head>
<meta charset="utf-8">
<title>Brightwell Digital Stationery</title>
<link rel="stylesheet" href="https://fonts.googleapis.com/css2?family=Arimo:wght@400;700&family=Oswald:wght@400;500&family=Questrial&display=swap">
<style>
:root{
  --green:#a9cd5d;
  --green-bg:#afd163;
  --ink:#474747;
  --ink-dark:#2f2f2f;
  --dark-block:#4a4748;
  --rule:#9a9a9a;
  --backdrop:#dedede;
  --page:#fbfbfb;
  --white:#ffffff;
}
*{margin:0;padding:0;box-sizing:border-box}
html,body{width:1200px;height:757px;overflow:hidden;background:var(--backdrop)}
body{position:relative;font-family:"Arimo",Arial,sans-serif;color:var(--ink)}
.page{position:absolute;background:var(--page);box-shadow:2px 2px 4px rgba(0,0,0,.35)}
.brand{font-family:"Questrial",sans-serif;color:var(--ink);line-height:1;white-space:nowrap}

/* Letterhead */
.letter{left:76px;top:61px;width:448px;height:630px;background:linear-gradient(180deg,#ffffff 0%,#f6f6f6 55%,#ececec 100%)}
.letter .brand{position:absolute;left:0;right:0;top:42px;text-align:center;font-size:30px}
.letter .tagline{position:absolute;left:160px;top:68px;font-family:"Questrial",sans-serif;font-size:7px;color:var(--ink)}
.letter .greeting{position:absolute;left:34px;top:157px;font-size:11px}
.letter .body{position:absolute;left:34px;top:189px;width:382px;font-size:6.4px;line-height:9.5px;color:#555;text-align:justify}
.letter .body p{margin-bottom:9.3px}
.letter .closing{position:absolute;left:34px;top:400px;font-size:6.4px;color:#555}
.letter .footer{position:absolute;left:0;right:0;top:589px;text-align:center;font-size:6.6px;line-height:11px;color:#777;letter-spacing:.2px}

/* Slides */
.slide{width:263px;height:197px}
.col-a{left:564px}.col-b{left:847px}
.row-1{top:61px}.row-2{top:275px}.row-3{top:493px}
.slide-head{position:absolute;left:14px;top:11px;font-family:"Oswald",sans-serif;font-weight:500;font-size:11px;color:var(--green);line-height:1}
.slide-sub{position:absolute;left:14px;top:25px;font-family:"Arimo",sans-serif;font-weight:700;font-size:5.6px;color:var(--ink-dark)}
.slide-rule{position:absolute;left:57px;right:14px;top:31px;height:.6px;background:var(--rule)}
.slide .mini-brand{position:absolute;right:14px;top:19px;font-size:9px}
.tiny{font-size:3.6px;line-height:5.2px;color:#444;text-align:justify}

/* Title slide */
.title-slide .brand{position:absolute;left:0;right:0;top:46px;text-align:center;font-size:34px}
.title-slide .tagline{position:absolute;left:52px;top:79px;font-family:"Questrial",sans-serif;font-size:7.6px;color:var(--ink)}
.title-slide .welcome{position:absolute;left:0;right:0;top:118px;text-align:center;font-family:"Oswald",sans-serif;line-height:1}
.welcome .w1{font-size:13px;color:var(--ink-dark);display:block}
.welcome .w2{font-size:15px;font-weight:500;color:var(--green);display:block;margin-top:3px}
.welcome .w3{font-size:12.5px;color:var(--ink-dark);display:block;margin-top:4px}

/* Team slide */
.photo{position:absolute;top:55px;width:51px;height:52px;background:var(--dark-block);border:1.5px solid #fff;box-shadow:0 0 1.5px rgba(0,0,0,.6);color:#ddd;font-size:6px;display:flex;align-items:center;justify-content:center}
.member{position:absolute;top:121px;width:50px}
.member .name{font-size:5px;color:var(--green)}
.member .role{font-size:5px;font-style:italic;color:#555;margin-top:2px}
.member .tiny{margin-top:6px}

/* Groups slide */
.group{position:absolute;width:114px}
.group h3{font-family:"Arimo",sans-serif;font-weight:400;font-size:5.8px;color:var(--green);margin-bottom:3px}

/* Chart slide */
.chart{position:absolute;left:25px;top:48px}
.chart-notes{position:absolute;left:159px;top:49px;width:90px;text-align:left}
.chart-notes p{margin-bottom:4px}
.chart-foot{position:absolute;left:21px;top:145px;width:218px}

/* Pie slide */
.pie-copy{position:absolute;left:17px;top:63px;width:114px;text-align:center}
.pie-copy p{margin-bottom:10px}
.pie{position:absolute;left:160px;top:52px}
.legend{position:absolute;left:162px;top:124px;width:72px}
.legend-item{display:flex;align-items:center;gap:4px;font-size:3.5px;color:#444;border-bottom:.5px solid #7a6b9a;padding:1.5px 0}
.swatch{width:4px;height:4px;display:inline-block}
.swatch.green{background:var(--green)}
.swatch.dark{background:var(--dark-block)}
.legend-note{position:absolute;left:162px;top:146px;width:80px;font-size:3.6px;line-height:5.2px;color:#444}

/* Thanks slide */
.thanks-slide{background:var(--green-bg)}
.thanks{position:absolute;left:0;right:0;top:66px;text-align:center;font-family:"Questrial",sans-serif;color:var(--white);line-height:1}
.thanks .big{display:block;font-size:39px}
.thanks .small{display:block;font-size:20px;margin-top:1px}
.thanks-contact{position:absolute;left:0;right:0;top:169px;text-align:center;font-size:4.4px;line-height:6.4px;color:var(--white)}
</style>
</head>
<body>

<!-- Letterhead -->
<section class="page letter">
  <div class="brand">brightwell</div>
  <div class="tagline">Right people, right place</div>
  <p class="greeting">Dear Mr. Smith,</p>
  <div class="body">
    <p>Lorem ipsum dolor sit amet, consectetur adipiscing elit. Donec orci purus, luctus vitae dignissim eu, iaculis sed purus. Vivamus faucibus, ipsum nec aliquet viverra, leo mauris condimentum ligula, sit amet sagittis enim ligula quis arcu. Nam egestas tortor id nisi porttitor mattis. In tortor ante, ultricies in suscipit a, tempus non massa. Vivamus et auctor mi. Fusce vel massa nulla. Phasellus nec eros mauris, et scelerisque orci.</p>
    <p>Donec malesuada orci vitae nulla accumsan porta a id massa. Quisque accumsan iaculis magna sit amet fringilla. Maecenas consequat, magna eget tincidunt semper, odio nibh rutrum mi, id feugiat ante nisi eu risus. Vestibulum nunc orci, rhoncus a placerat in, ultricies in mi. Cras mattis varius eros, vel fringilla nisi suscipit eget. Quisque scelerisque sagittis nulla at porttitor.</p>
    <p>Sed id augue vitae urna euismod commodo aliquet a quam. Pellentesque arcu velit, cursus et malesuada ut, consequat et diam. Nullam erat sem, rhoncus id ullamcorper vitae, rhoncus et arcu. In ultricies ultricies nulla, ut rutrum nisi iaculis at. Donec eu magna a metus ornare faucibus. Fusce aliquet faucibus ultricies. Morbi semper, est id tincidunt gravida, sem arcu adipiscing lacus, ac bibendum nulla leo eu purus. Quisque nec diam sed risus consectetur a cumsan quis quis nibh. Vestibulum id purus lorem.</p>
    <p>It is a long established fact that a reader will be distracted by the readable content of a page when looking at its layout. The point of using Lorem Ipsum is that it has a more-or-less normal distribution of letters, as opposed to using 'Content here, content here', making it look like readable English. Many desktop publishing packages</p>
    <p>ada ut, consequat et diam. Nullam erat sem, rhoncus id ullamcorper vitae, rhoncus et arcu. In ultricies ultricies nulla, ut rutrum nisi iaculis at. Donec eu magna a metus ornare faucibus. Fusce aliquet faucibus ultricies. Morbi semper,</p>
  </div>
  <p class="closing">Sincerely,</p>
  <div class="footer">
    P. 555-014-2287 C. 555-018-6630 E. hello@brightwell-talent.com W. www.brightwell-talent.com<br>
    214 Harlow Street, Maple Ridge, Oregon 97810
  </div>
</section>

<!-- Title slide -->
<section class="page slide title-slide col-a row-1">
  <div class="brand">brightwell</div>
  <div class="tagline">Right people, right place</div>
  <div class="welcome">
    <span class="w1">Welcome to Our</span>
    <span class="w2">Presentation Name</span>
    <span class="w3">Description</span>
  </div>
</section>

<!-- Team slide -->
<section class="page slide col-b row-1">
  <h2 class="slide-head">Heading Here</h2>
  <div class="slide-sub">Sub Heading</div>
  <div class="slide-rule"></div>
  <div class="brand mini-brand">brightwell</div>
  <div class="photo" style="left:19px" role="img" aria-label="Portrait photo of team member 1">Photo</div>
  <div class="photo" style="left:77px" role="img" aria-label="Portrait photo of team member 2">Photo</div>
  <div class="photo" style="left:135px" role="img" aria-label="Portrait photo of team member 3">Photo</div>
  <div class="photo" style="left:193px" role="img" aria-label="Portrait photo of team member 4">Photo</div>
  <div class="member" style="left:21px"><div class="name">Team member1</div><div class="role">Title</div><p class="tiny">Lorem ipsum dolor sit amet, consectetur adipisicing elit, sed do eiusmod tempor incididunt</p></div>
  <div class="member" style="left:79px"><div class="name">Team member2</div><div class="role">Title</div><p class="tiny">ut labore et dolore magna aliqua. Ut enim ad minim veniam, quis nostrud exercitation</p></div>
  <div class="member" style="left:137px"><div class="name">Team member3</div><div class="role">Title</div><p class="tiny">ullamco laboris nisi ut aliquip ex ea commodo consequat. Enim ad minim veniam,</p></div>
  <div class="member" style="left:195px"><div class="name">Team member4</div><div class="role">Title</div><p class="tiny">Do eiusmod tempor incididunt. Lorem ipsum dolor sit amet, consectetur adipisicing elit, sed</p></div>
</section>

<!-- Groups slide -->
<section class="page slide col-a row-2">
  <h2 class="slide-head">Heading Here</h2>
  <div class="slide-sub">Sub Heading</div>
  <div class="slide-rule"></div>
  <div class="brand mini-brand">brightwell</div>
  <div class="group" style="left:16px;top:52px"><h3>Group1</h3><p class="tiny">Lorem ipsum dolor sit amet, consectetur adipisicing elit, sed do eiusmod tempor incididunt ut labore et dolore magna aliqua. Ut enim ad minim veniam, quis nostrud exercitation ullamco laboris nisi ut aliquip ex ea commodo consequat.</p></div>
  <div class="group" style="left:16px;top:97px"><h3>Group2</h3><p class="tiny">Duis aute irure dolor in reprehenderit in voluptate velit esse cillum dolore eu fugiat nulla pariatur. Excepteur sint occaecat cupidatat non proident, sunt in culpa qui officia deserunt mollit anim id est laborum.</p></div>
  <div class="group" style="left:16px;top:138px"><h3>Group3</h3><p class="tiny">Duis aute irure dolor in reprehenderit in voluptate velit esse cillum dolore eu fugiat nulla pariatur. Excepteur sint occaecat cupidatat non proident, sunt in culpa qui officia deserunt mollit anim id est laborum.</p></div>
  <div class="group" style="left:135px;top:52px"><h3>Group4</h3><p class="tiny">Lorem ipsum dolor sit amet, consectetur adipisicing elit, sed do eiusmod tempor incididunt ut labore et dolore magna aliqua. Ut enim ad minim veniam, quis nostrud exercitation ullamco laboris nisi ut aliquip ex ea commodo consequat.</p></div>
  <div class="group" style="left:135px;top:97px"><h3>Group5</h3><p class="tiny">Duis aute irure dolor in reprehenderit in voluptate velit esse cillum dolore eu fugiat nulla pariatur. Excepteur sint occaecat cupidatat non proident, sunt in culpa qui officia deserunt mollit anim id est laborum.</p></div>
  <div class="group" style="left:135px;top:138px"><h3>Group6</h3><p class="tiny">Duis aute irure dolor in reprehenderit in voluptate velit esse cillum dolore eu fugiat nulla pariatur. Excepteur sint occaecat cupidatat non proident, sunt in culpa qui officia deserunt mollit anim id est laborum.</p></div>
</section>

<!-- Bar chart slide -->
<section class="page slide col-b row-2">
  <h2 class="slide-head">Heading Here</h2>
  <div class="slide-sub">Sub Heading</div>
  <div class="slide-rule"></div>
  <div class="brand mini-brand">brightwell</div>
  <svg class="chart" width="106" height="82" viewBox="0 0 106 82" aria-label="Bar chart of four values">
    <g stroke="#d6d6d6" stroke-width=".5">
      <line x1="0" y1="1" x2="104" y2="1"/><line x1="0" y1="9" x2="104" y2="9"/>
      <line x1="0" y1="17" x2="104" y2="17"/><line x1="0" y1="25" x2="104" y2="25"/>
      <line x1="0" y1="33" x2="104" y2="33"/><line x1="0" y1="41" x2="104" y2="41"/>
      <line x1="0" y1="49" x2="104" y2="49"/><line x1="0" y1="57" x2="104" y2="57"/>
      <line x1="0" y1="65" x2="104" y2="65"/><line x1="0" y1="73" x2="104" y2="73"/>
      <line x1="0" y1="80" x2="104" y2="80"/>
    </g>
    <g fill="#a9cd5d">
      <rect x="24" y="4" width="13" height="76"/>
      <rect x="40" y="15" width="13" height="65"/>
      <rect x="55" y="34" width="13" height="46"/>
      <rect x="72" y="20" width="13" height="60"/>
    </g>
    <g fill="#fff" font-family="Arimo, sans-serif" font-size="4">
      <text transform="translate(33 77) rotate(-90)">Sub text1</text>
      <text transform="translate(49 77) rotate(-90)">Sub text2</text>
      <text transform="translate(64 77) rotate(-90)">Sub text3</text>
      <text transform="translate(81 77) rotate(-90)">Sub text4</text>
    </g>
  </svg>
  <div class="chart-notes tiny">
    <p>Lorem ipsum dolor sit amet, consectetur adipisicing elit, sed do eiusmod tempor incididunt ut labore et dolore magna aliqua. Ut enim ad minim veniam, quis nostrud.</p>
    <p>consectetur adipisicing elit, sed do eiusmod tempor incididunt ut labore Lorem ipsum dolor sit amet, et dolore magna aliqua. Ut enim ad minim veniam, quis nostrud.</p>
  </div>
  <p class="chart-foot tiny">Lorem ipsum dolor sit amet, consectetur adipisicing elit, sed do eiusmod tempor incididunt ut labore et dolore magna aliqua. Ut enim ad minim veniam, quis nostrud exercitation ullamco laboris nisi ut aliquip ex ea commodo consequat. Duis aute irure dolor in reprehenderit in voluptate velit esse cillum dolore eu fugiat nulla pariatur. Excepteur sint occaecat cupidatat non proident, sunt in culpa qui officia deserunt mollit anim id est laborum.</p>
</section>

<!-- Pie chart slide -->
<section class="page slide col-a row-3">
  <h2 class="slide-head">Heading Here</h2>
  <div class="slide-sub">Sub Heading</div>
  <div class="slide-rule"></div>
  <div class="brand mini-brand">brightwell</div>
  <div class="pie-copy tiny" style="text-align:center">
    <p>Lorem ipsum dolor sit amet, consectetur adipisicing elit, sed do eiusmod tempor incididunt ut labore et dolore magna aliqua. Ut enim ad minim veniam, quis nostrud exercitation ullamco laboris nisi ut aliquip ex ea commodo consequat. Duis aute irure dolor in reprehenderit in voluptate velit esse cillum dolore eu fugiat nulla pariatur. Excepteur sint occaecat cupidatat non proident, sunt in culpa qui officia deserunt mollit anim id est laborum. Ut enim ad minim veniam, quis nostrud exercitation ullamco laboris nisi ut aliquip ex ea commodo consequat.</p>
    <p>Excepteur sint occaecat cupidatat non proident, sunt in culpa qui officia deserunt mollit anim id est laborum. Ut enim ad minim veniam, quis nostrud exercitation ullamco laboris nisi ut aliquip ex ea commodo consequat.</p>
  </div>
  <svg class="pie" width="66" height="66" viewBox="-33 -33 66 66" aria-label="Pie chart split between two values">
    <path d="M0 0 L-2.5 -28.9 A29 29 0 0 1 23.8 -16.6 Z" fill="#4a4748"/>
    <path d="M2 0 L25.8 -16.6 A29 29 0 0 1 30 7.5 Z" fill="#a9cd5d"/>
    <path d="M0 0 L28 7.5 A29 29 0 0 1 12.3 26.3 Z" fill="#4a4748"/>
    <path d="M0 0 L12.3 26.3 A29 29 0 1 1 -2.5 -28.9 Z" fill="#a9cd5d"/>
  </svg>
  <div class="legend">
    <div class="legend-item"><span class="swatch green"></span>Lorem ipsum dolor sit amet 50%</div>
    <div class="legend-item"><span class="swatch dark"></span>Duis aute irure dolor in 50%</div>
  </div>
  <p class="legend-note">sunt in culpa qui officia deserunt mollit anim id est laborum. Ut enim ad minim veniam</p>
</section>

<!-- Closing slide -->
<section class="page slide thanks-slide col-b row-3">
  <div class="thanks">
    <span class="big">Thanks</span>
    <span class="small">For Coming</span>
  </div>
  <div class="thanks-contact">
    214 Harlow Street, Maple Ridge, Oregon 97810<br>
    P : 555-014-2287 M : 555-018-663 E : hello@brightwell-talent.com W : www.brightwell-talent.com
  </div>
</section>

</body>
</html>
```